Newly opened kids play space needs brochure to show what our space has to offer

Tri-fold color brochure with same aethetic as website (www.fernhollowplayhouse.com) that provides a comprehensive and visual overview of what our play space is comprised of. Features of the brochure should include our logo, "A Garrick and Pellinger-inspired Play Space in the Poconos", photos of: Dedicated Infant Play Area; Cafe and Free WiFi; Weekly Themed Activities; Unique Classes; Parties and Events. Photos also of our open play area with children playing within it. Info within the brochure should include our location, hours. Please take some copy from : https://www.facebook.com/fernhollowtinkerplayhouse/?ref=bookmarks
and from the Plan Your Visit part of the website. I have a lot of photos to use; is there a way to put in generic photo placeholders and I can pick which photos of mine to go into the various areas of the brochure, or if you need the photos ahead of time, please let me know the best way to proceed. I am attaching the logo files for now.

Font styles to use
Sans Serif

Colors
85cae6
cee9f5
86cfc6
cfeae6
fdf9cf
fff3d1
eaf2ce
cadf82

Requirements
Must have
• Eye catching placement of photos; color scheme similar to website and logo colors
Should not have
• Brochure should be simple, not too colorful - no primary colors, not too crowded.

```html
<!DOCTYPE html>
<html lang="en">
<head>
<meta charset="utf-8">
<title>Fern Hollow Playhouse – Tri-fold Brochure</title>
<link rel="stylesheet" href="https://fonts.googleapis.com/css2?family=Open+Sans:wght@400;600&family=Roboto+Condensed:wght@400;700&family=Archivo:wght@800&display=swap">
<style>
:root{
  --stage:#a7a8aa;
  --paper:#ffffff;
  --blue:#1b8cbf;
  --blue-deep:#14739f;
  --pink:#e2566f;
  --green:#8cc43f;
  --green-soft:#b9da7c;
  --ink:#2a2a2a;
  --muted:#555;
}
*{box-sizing:border-box;margin:0;padding:0}
html,body{width:877px;height:1200px;overflow:hidden;background:var(--stage)}
body{position:relative;font-family:"Open Sans",Arial,sans-serif;color:var(--ink)}
.sheet{position:absolute;left:106px;width:665px;height:515px;background:var(--paper);box-shadow:0 8px 10px rgba(0,0,0,.3);overflow:hidden}
.sheet--outside{top:59px}
.sheet--inside{top:612px}
.sheet svg.art{position:absolute;left:0;top:0;width:665px;height:515px}
.layer{position:absolute}
.display{font-family:"Archivo",Arial,sans-serif;font-weight:800}
.brand{font-family:"Open Sans",Arial,sans-serif;font-weight:600;color:var(--blue);white-space:nowrap;display:flex;align-items:center;gap:6px}
.brand__dot{width:12px;height:12px;border-radius:50%;background:var(--green);flex:none}
.brand__tag{font-size:6px;color:var(--blue);text-align:center}
.price{left:69px;top:44px;width:94px;text-align:center;color:#fff;line-height:1}
.price b{display:block;font-size:25px;font-weight:800}
.price span{display:block;font-size:10px;margin-top:2px;line-height:1.15}
.plan{left:219px;top:190px;width:219px;text-align:center;color:#fff;padding:0 14px}
.plan h2{font-size:16px;margin-bottom:9px;letter-spacing:.2px}
.plan p{font-size:10px;line-height:1.38}
.head{font-family:"Roboto Condensed",Arial,sans-serif;font-size:17px;line-height:1;white-space:nowrap}
.head em{font-style:normal;background:var(--pink);color:#fff;padding:1px 2px 1px 3px}
.head span{color:var(--blue)}
.rule{height:1px;background:linear-gradient(90deg,var(--green),rgba(140,196,63,0));margin-top:3px}
.copy{font-size:10px;line-height:1.33;text-align:justify}
.contact{left:245px;top:386px;width:190px;font-size:9px;line-height:1.3}
.contact li{list-style:none;display:flex;gap:7px;align-items:flex-start;margin-bottom:6px}
.contact li.small{font-size:7.5px}
.contact svg{flex:none;width:11px;height:11px;margin-top:1px}
.pill{height:18px;border-radius:9px;color:#fff;font-size:10px;letter-spacing:.8px;display:flex;align-items:center;justify-content:center;white-space:nowrap}
.pill--pink{background:var(--pink)}
.pill--blue{background:var(--blue)}
.motto{left:504px;top:303px;width:104px;text-align:center;color:#fff;font-size:16px;line-height:1.35}
.intro{left:438px;top:404px;width:227px;text-align:center;line-height:1.12}
.intro .l1{font-family:"Roboto Condensed",Arial,sans-serif;font-size:16px;color:var(--blue)}
.intro .l2{font-size:13.5px;color:var(--pink);letter-spacing:.5px}
.intro .l3{font-size:13.5px;color:var(--green)}
.days{font-family:"Roboto Condensed",Arial,sans-serif;font-size:16px;color:var(--green);line-height:1}
.time{font-size:10px;margin-top:3px}
</style>
</head>
<body>

<section class="sheet sheet--outside">
  <svg class="art" viewBox="0 0 665 515">
    <defs>
      <linearGradient id="foldShade" x1="0" x2="1">
        <stop offset="0" stop-color="#000" stop-opacity=".07"/>
        <stop offset=".12" stop-color="#000" stop-opacity="0"/>
        <stop offset=".88" stop-color="#000" stop-opacity="0"/>
        <stop offset="1" stop-color="#000" stop-opacity=".05"/>
      </linearGradient>
      <linearGradient id="blueBand" x1="0" y1="0" x2="0" y2="1">
        <stop offset="0" stop-color="#1f93c4"/>
        <stop offset="1" stop-color="#167aa8"/>
      </linearGradient>
      <linearGradient id="photoWarm" x1="0" y1="0" x2="1" y2="1">
        <stop offset="0" stop-color="#6e5a4c"/>
        <stop offset=".5" stop-color="#b78a5c"/>
        <stop offset="1" stop-color="#4b3a33"/>
      </linearGradient>
      <linearGradient id="photoKids" x1="0" y1="0" x2="1" y2="0">
        <stop offset="0" stop-color="#e9a98c"/>
        <stop offset=".5" stop-color="#d98b6e"/>
        <stop offset="1" stop-color="#5a9c5e"/>
      </linearGradient>
      <linearGradient id="photoTable" x1="0" y1="0" x2="1" y2="1">
        <stop offset="0" stop-color="#9ea3a8"/>
        <stop offset=".55" stop-color="#c9b38a"/>
        <stop offset="1" stop-color="#d8c35a"/>
      </linearGradient>
      <clipPath id="outBand">
        <path d="M0,88 C200,150 450,160 665,70 L665,385 C480,300 180,300 0,385 Z"/>
      </clipPath>
    </defs>

    <g clip-path="url(#outBand)">
      <rect role="img" aria-label="Photo: children and a teacher dancing with arms raised in the open play area" x="0" y="60" width="219" height="330" fill="url(#photoWarm)"/>
      <rect x="219" y="143" width="219" height="250" fill="url(#blueBand)"/>
      <rect role="img" aria-label="Photo: children gathered around a table with flowers and natural toys" x="438" y="60" width="227" height="330" fill="url(#photoTable)"/>
    </g>
    <rect role="img" aria-label="Photo: three smiling children with painted hands giving a thumbs up" x="250" y="24" width="160" height="119" rx="6" fill="url(#photoKids)"/>

    <path d="M0,88 C200,150 450,160 665,70" fill="none" stroke="#fff" stroke-width="6"/>
    <path d="M0,82 C200,144 450,154 665,64" fill="none" stroke="var(--green)" stroke-width="4"/>
    <path d="M0,385 C180,300 480,300 665,385" fill="none" stroke="#fff" stroke-width="6"/>
    <path d="M0,392 C180,307 480,307 665,392" fill="none" stroke="var(--green)" stroke-width="4"/>

    <circle cx="116" cy="85" r="52" fill="#fff"/>
    <path d="M70,105 A52,52 0 0 1 150,40" fill="none" stroke="var(--green)" stroke-width="3"/>
    <circle cx="116" cy="85" r="46" fill="var(--blue)"/>

    <circle cx="556" cy="343" r="58" fill="#fff"/>
    <path d="M500,352 A58,58 0 0 0 612,352" fill="none" stroke="var(--green)" stroke-width="3"/>
    <circle cx="556" cy="343" r="52" fill="var(--pink)"/>

    <rect x="0" y="0" width="219" height="515" fill="url(#foldShade)"/>
    <rect x="219" y="0" width="219" height="515" fill="url(#foldShade)"/>
    <rect x="438" y="0" width="227" height="515" fill="url(#foldShade)"/>
  </svg>

  <div class="layer price display"><b>$12</b><span>Daily<br>Admission</span></div>

  <div class="layer" style="left:12px;top:404px;width:200px">
    <div class="head"><em>ABOUT</em><span> US</span></div>
    <p class="copy" style="margin-top:10px">We are a Pellinger and Garrick inspired play space, offering a variety of play groups, recreational classes, and natural toys that foster open ended play.</p>
  </div>

  <div class="layer plan">
    <h2 class="display">PLAN YOUR VISIT!</h2>
    <p>Fern Hollow offers open-ended, natural toys and activities that nurture the child's sense of wonder and invites them to explore in our serene and spacious environment.</p>
  </div>

  <div class="layer" style="left:219px;top:338px;width:219px;text-align:center">
    <div class="brand" style="justify-content:center;font-size:21px"><i class="brand__dot"></i>fern hollow</div>
    <div class="brand__tag">A Garrellinger Play Space</div>
  </div>

  <ul class="layer contact">
    <li><svg viewBox="0 0 12 12"><circle cx="6" cy="6" r="6" fill="var(--green)"/><path d="M6 2.5a2.2 2.2 0 0 1 2.2 2.2C8.2 6.4 6 9.3 6 9.3S3.8 6.4 3.8 4.7A2.2 2.2 0 0 1 6 2.5z" fill="#fff"/></svg><span>48 Larkmoor Rd<br>Hollisburg, Pennsylvania</span></li>
    <li><svg viewBox="0 0 12 12"><circle cx="6" cy="6" r="6" fill="var(--green)"/><path d="M4 3.2l1.2 1.3-.6.8c.4.9 1.1 1.6 2 2l.8-.6 1.3 1.2-.7 1c-2.5-.2-4.7-2.4-4.9-4.9z" fill="#fff"/></svg><span>+1 555-014-2290</span></li>
    <li class="small"><svg viewBox="0 0 12 12"><circle cx="6" cy="6" r="6" fill="var(--green)"/></svg><span>m.me/fernhollowtinkerplayhouse</span></li>
    <li class="small"><svg viewBox="0 0 12 12"><circle cx="6" cy="6" r="6" fill="var(--green)"/></svg><span>www.pictagram.com/fernhollowplayhouse/</span></li>
  </ul>

  <div class="layer pill pill--pink" style="left:246px;top:491px;width:180px">www.fernhollowplayhouse.com</div>

  <div class="layer" style="left:438px;top:55px;width:227px;text-align:center">
    <div class="brand" style="justify-content:center;font-size:30px"><i class="brand__dot"></i>fern hollow</div>
    <div class="brand__tag" style="font-size:7px">A Garrellinger Play Space</div>
  </div>

  <div class="layer motto display">Play.<br>Learn.<br>Grow.</div>

  <div class="layer intro">
    <div class="l1">We are a Garrick and</div>
    <div class="l2 display">PELLINGER-INSPIRED<br>PLAY SPACE</div>
    <div class="l3 display">located in the Poconos.</div>
  </div>

  <div class="layer pill pill--blue" style="left:464px;top:491px;width:173px">www.fernhollowplayhouse.com</div>
</section>

<section class="sheet sheet--inside">
  <svg class="art" viewBox="0 0 665 515">
    <defs>
      <linearGradient id="pCafe" x1="0" y1="0" x2="1" y2="1"><stop offset="0" stop-color="#7a6a5c"/><stop offset="1" stop-color="#b0946e"/></linearGradient>
      <linearGradient id="pGarden" x1="0" y1="0" x2="1" y2="1"><stop offset="0" stop-color="#8a8f8e"/><stop offset="1" stop-color="#6b5a48"/></linearGradient>
      <linearGradient id="pBlocks" x1="0" y1="0" x2="1" y2="1"><stop offset="0" stop-color="#b7a594"/><stop offset="1" stop-color="#d9c0a0"/></linearGradient>
      <linearGradient id="pInfant" x1="0" y1="0" x2="1" y2="1"><stop offset="0" stop-color="#d7b09a"/><stop offset="1" stop-color="#a88a76"/></linearGradient>
      <linearGradient id="pCircle" x1="0" y1="0" x2="1" y2="1"><stop offset="0" stop-color="#a58a82"/><stop offset="1" stop-color="#c26a82"/></linearGradient>
      <linearGradient id="pSilks" x1="0" y1="0" x2="1" y2="1"><stop offset="0" stop-color="#5c4f9c"/><stop offset="1" stop-color="#8e3f9a"/></linearGradient>
      <clipPath id="inTop"><path d="M0,0 H665 V150 C450,210 200,205 0,146 Z"/></clipPath>
      <clipPath id="inBottom"><path d="M0,405 C200,385 460,383 665,409 V515 H0 Z"/></clipPath>
    </defs>

    <g clip-path="url(#inTop)">
      <rect role="img" aria-label="Photo: a parent enjoying coffee in the cafe lounge" x="0" y="0" width="217" height="220" fill="url(#pCafe)"/>
      <rect role="img" aria-label="Photo: hands planting flowers in soil during a themed activity" x="223" y="0" width="218" height="220" fill="url(#pGarden)"/>
      <rect role="img" aria-label="Photo: a child playing with a wooden play house" x="447" y="0" width="218" height="220" fill="url(#pBlocks)"/>
    </g>
    <path d="M0,146 C200,205 450,210 665,150" fill="none" stroke="#fff" stroke-width="5"/>
    <path d="M0,153 C200,212 450,217 665,157" fill="none" stroke="var(--green)" stroke-width="4"/>

    <g clip-path="url(#inBottom)">
      <rect role="img" aria-label="Photo: a mother and baby in the infant area" x="0" y="380" width="217" height="135" fill="url(#pInfant)"/>
      <rect role="img" aria-label="Photo: children and teachers sitting in a circle during class" x="223" y="380" width="218" height="135" fill="url(#pCircle)"/>
      <rect role="img" aria-label="Photo: children playing under colourful play silks" x="447" y="380" width="218" height="135" fill="url(#pSilks)"/>
    </g>
    <path d="M0,405 C200,385 460,383 665,409" fill="none" stroke="#fff" stroke-width="5"/>
    <path d="M0,399 C200,379 460,377 665,403" fill="none" stroke="var(--green)" stroke-width="4"/>

    <g>
      <circle cx="105" cy="166" r="30" fill="#fff"/><circle cx="105" cy="166" r="26" fill="var(--blue)"/>
      <circle cx="332" cy="180" r="30" fill="#fff"/><circle cx="332" cy="180" r="26" fill="var(--blue)"/>
      <circle cx="556" cy="166" r="30" fill="#fff"/><circle cx="556" cy="166" r="26" fill="var(--blue)"/>
    </g>
  </svg>

  <div class="layer" style="left:16px;top:216px;width:200px">
    <div class="head"><em>CAFE</em><span> AND WIFI</span></div>
    <div class="rule"></div>
    <p class="copy" style="margin-top:8px">Take a break or catch up on work while enjoying Brewmont coffee, beverages, and healthy snacks.</p>
  </div>
  <div class="layer" style="left:16px;top:312px;width:200px">
    <div class="head"><em>DEDICATED</em><span> INFANT AREA</span></div>
    <div class="rule"></div>
    <p class="copy" style="margin-top:8px;text-align:left">Bond safely with your baby while being within eyeshot of the main play area.</p>
  </div>

  <div class="layer" style="left:228px;top:218px;width:205px">
    <div class="head"><em>THEMED</em><span> ACTIVITIES</span></div>
    <div class="rule"></div>
    <p class="copy" style="margin-top:8px">Stories, crafts, and activities change weekly to celebrate the seasons and the world around us.</p>
  </div>
  <div class="layer" style="left:228px;top:306px;width:205px">
    <div class="head"><em>UNIQUE</em><span> CLASSES</span></div>
    <div class="rule"></div>
    <p class="copy" style="margin-top:8px">Our multi-age, multi-sensory approach to traditional classes nurtures the whole child in a creative and fun way.</p>
  </div>

  <div class="layer" style="left:450px;top:210px;width:200px">
    <div class="head"><em>OPEN</em><span> PLAY</span></div>
    <div class="rule"></div>
    <div class="days" style="margin-top:7px">Mon, Wed, Fri, Sun</div>
    <div class="time">10:00AM - 5:00PM</div>
    <div class="days" style="margin-top:8px">Tue, Thu, Sat</div>
    <div class="time" style="margin-top:6px">10:00AM - 7:00PM</div>
  </div>
  <div class="layer" style="left:450px;top:326px;width:200px">
    <div class="head"><em>INFANTS</em><span> ONLY</span></div>
    <div class="rule"></div>
    <div class="days" style="margin-top:6px">Monday through Friday</div>
    <div class="time">9:00AM - 10:00AM</div>
  </div>
</section>

</body>
</html>
```